Quellbrin.ca Your Canadian Source for all your mortgage needs.

I need to get a fresh look on my current website. It is not currently a Wordpress site and i need to build a whole new site that i can do my editing in using Wordpress.
I need it built in a mobile or responsive theme.
There will be a secured application page which is critical.
I have 3 books written so i want to be able to have advertising spaces for promoting them and a landing page ( I can build my own landing pages)
I need the frame work of a professional theme with easy editing capabilities.
I have my own LOGOs which i would continue to use. The current site can be reviewed at www.quellbrin.ca.
The front page could have a young couple near a nice house, open to suggestions.
I don't need a blog post to update but if it was on the sides of the pages I could use it. Something like a "Latest News" section.
I would like to have a Main page, Application Page, Resource page, Contact page, Calculator Page, a questions and answer page. Theses can be populated with the current information or I can add latter.
I want the main page to be a mini sales page so I can link to Posts on First Time Home Buyers, Refinance Options, Second Home or New purchase options.
I provide mortgages for people across Canada so i want the Canadian Flag incorporated
I like the colors to work with the logo colors on the current site

Canadian Mortgage Clients

Sans Serif

3277b5
cadf82

• Must work in a Wordpress Theme
• Please see Project description for more details
• Space to add banner ads for my books. I have 3 books written

```html
<!DOCTYPE html>
<html lang="en">
<head>
<meta charset="utf-8">
<title>Quellbrin.ca – Your Canadian Source for all your mortgage needs</title>
<link href="https://fonts.googleapis.com/css2?family=Open+Sans:wght@400;600;700&family=Roboto:wght@400;500;700&display=swap" rel="stylesheet">
<style>
:root{
  --blue:#3277b5;
  --blue-dark:#1f5a8f;
  --green:#2fb35a;
  --lime:#cadf82;
  --orange:#f39a1d;
  --ink:#2b2f33;
  --muted:#6d747b;
  --line:#e3e6e9;
  --footer:#1c2730;
  --footer-2:#151e25;
  --white:#fff;
}
*{box-sizing:border-box;margin:0;padding:0}
html,body{width:1200px;height:2480px;overflow:hidden;background:#fff}
body{font-family:"Open Sans",Arial,sans-serif;color:var(--ink);position:relative}
.btn{display:inline-block;border:none;color:#fff;font:600 13px "Open Sans",sans-serif;border-radius:3px;text-align:center}

/* hero */
.hero{position:absolute;left:0;top:0;width:1200px;height:530px;background:linear-gradient(120deg,#2c4563 0%,#4d6a86 35%,#9b7a5f 62%,#5a6f84 100%)}
.hero-shade{position:absolute;inset:0;background:linear-gradient(180deg,rgba(15,30,50,.35),rgba(15,30,50,.15) 60%,rgba(15,30,50,.45))}
.topbar{position:absolute;left:0;top:0;width:1200px;height:62px;background:rgba(20,35,55,.55);display:flex;align-items:center;padding:0 60px}
.brand{display:flex;align-items:center;gap:8px;font:700 26px "Roboto",sans-serif;color:#fff}
.brand-dot{width:16px;height:16px;background:var(--lime)}
.nav{margin-left:auto;display:flex;align-items:center;gap:30px;font:500 13px "Roboto",sans-serif;color:#fff}
.nav .pill{border:1px solid rgba(255,255,255,.7);padding:6px 14px;border-radius:2px}
.nav .phone{background:var(--green);padding:8px 16px;border-radius:2px;font-weight:700}
.hero-copy{position:absolute;left:80px;top:200px;width:560px;color:#fff}
.hero-copy h1{font:700 44px "Roboto",sans-serif;margin-bottom:10px}
.hero-copy p{font-size:19px;line-height:1.3}
.finder{position:absolute;left:708px;top:170px;width:432px;height:258px;background:rgba(30,45,65,.82);padding:18px 22px;color:#fff}
.finder h2{font:600 18px "Roboto",sans-serif;margin-bottom:14px}
.field-row{display:flex;gap:10px;margin-bottom:10px}
.field{flex:1;height:30px;background:#fff;border-radius:2px;font-size:11px;color:#8b9097;padding:8px 10px}
.select-wrap{display:flex;gap:10px;align-items:flex-start}
.select{width:194px;background:#fff;border-radius:2px}
.select .head{height:30px;font-size:11px;color:#8b9097;padding:8px 10px;border-bottom:1px solid var(--line)}
.select .opt{font-size:11px;color:#fff;background:var(--blue);padding:6px 10px;border-bottom:1px solid rgba(255,255,255,.25)}
.finder .apply{width:184px;height:30px;line-height:30px;background:var(--green)}
.trust{position:absolute;left:0;top:488px;width:1200px;height:42px;background:rgba(18,32,48,.85);display:flex;align-items:center;padding:0 60px;color:#dfe6ee;font-size:12px}
.trust .ico{width:22px;height:22px;border-radius:50%;background:var(--green);margin-right:12px}
.trust .cta{margin-left:auto;font-weight:700;color:#fff}

/* section titles */
.sec-title{position:absolute;left:0;width:1200px;text-align:center;font:500 24px "Roboto",sans-serif;color:var(--ink);letter-spacing:.5px}
.sec-title::after{content:"";display:block;width:60px;height:3px;background:var(--blue);margin:10px auto 0}

/* why */
.why-card{position:absolute;top:660px;width:340px;height:360px;background:#fff;border:1px solid var(--line)}
.why-card .photo{height:160px}
.why-card .tag{display:inline-block;margin:-18px 0 0 12px;position:relative;background:var(--blue);color:#fff;font:600 12px "Open Sans",sans-serif;padding:6px 12px}
.why-card p{font-size:12px;line-height:1.6;color:var(--muted);padding:12px 18px 0}
.why-card .btn{position:absolute;left:110px;bottom:10px;width:120px;height:30px;line-height:30px;background:var(--footer)}

/* are you */
.areyou{position:absolute;left:0;top:1060px;width:1200px;height:450px;background:linear-gradient(180deg,#8fb1cf 0%,#c9d3c4 45%,#7c8a66 100%)}
.areyou::before{content:"";position:absolute;inset:0;background:rgba(255,255,255,.25)}
.areyou h2{position:absolute;top:40px;left:0;width:1200px;text-align:center;font:500 24px "Roboto",sans-serif;color:var(--ink)}
.areyou h2::after{content:"";display:block;width:60px;height:3px;background:var(--blue);margin:10px auto 0}
.role{position:absolute;top:110px;width:300px;height:240px;background:rgba(255,255,255,.92);text-align:center;padding-top:30px}
.role .badge{width:60px;height:60px;border-radius:50%;background:var(--green);margin:0 auto 14px;display:flex;align-items:center;justify-content:center}
.role h3{font:700 15px "Roboto",sans-serif;color:var(--ink);margin-bottom:10px}
.role p{font-size:12px;line-height:1.6;color:var(--muted);padding:0 26px}
.role-btn{position:absolute;top:370px;width:110px;height:34px;line-height:34px}

/* property */
.prop{position:absolute;width:254px;height:210px;background:#fff;border:1px solid var(--line)}
.prop .photo{height:160px;position:relative}
.prop .corner{position:absolute;left:0;top:0;width:0;height:0;border-top:34px solid var(--orange);border-right:34px solid transparent}
.prop .meta{display:flex;align-items:center;justify-content:space-between;padding:14px 10px}
.prop .name{font:500 13px "Roboto",sans-serif;color:var(--ink)}
.prop .view{background:var(--blue);font-size:10px;padding:5px 8px}

/* footer */
.footer{position:absolute;left:0;top:2110px;width:1200px;height:370px;background:var(--footer);color:#c5ced6}
.footer .brand{position:absolute;left:60px;top:60px}
.fcol{position:absolute;top:70px;font-size:12px;line-height:2}
.fcol h4{font:600 14px "Roboto",sans-serif;color:#fff;margin-bottom:6px}
.join{position:absolute;left:260px;top:270px;display:flex;align-items:center;gap:10px;font-size:13px;color:#fff}
.join span.c{width:22px;height:22px;border-radius:50%;background:#7f8c97}
.subscribe{position:absolute;left:680px;top:266px;display:flex;align-items:center;gap:14px;font-size:13px;color:#fff}
.subscribe .in{width:200px;height:30px;background:#fff;border-radius:2px;color:#8b9097;font-size:11px;padding:8px 10px}
.subscribe .go{background:var(--blue);width:50px;height:30px;line-height:30px}
.copy{position:absolute;left:0;bottom:0;width:1200px;height:50px;background:var(--footer-2);font-size:11px;color:#8d98a2;padding:18px 60px}
</style>
</head>
<body>

<header class="hero">
  <div class="hero-shade" role="img" aria-label="Photo of a modern house at dusk with warm lit windows"></div>
  <div class="topbar">
    <div class="brand"><span class="brand-dot"></span>Quellbrin</div>
    <nav class="nav">
      <span>Home</span><span>Services</span><span>Mortgage</span><span>Calculator</span>
      <span class="pill">Contact Us</span><span class="pill">Menu</span>
      <span class="phone">1-800-555-0142</span>
    </nav>
  </div>
  <div class="hero-copy">
    <h1>Welcome to Northhaven</h1>
    <p>Contrary to popular belief, Lorem Ipsum is not simply random text. It has roots in a piece of classical Latin literature from 45 BC, making it over 2000 years old.</p>
  </div>
  <form class="finder">
    <h2>Find a Mortgage</h2>
    <div class="field-row"><div class="field">First Name</div><div class="field">Last Name</div></div>
    <div class="field-row"><div class="field">Email</div><div class="field">Phone</div></div>
    <div class="select-wrap">
      <div class="select">
        <div class="head">I am a ▾</div>
        <div class="opt">Developer</div>
        <div class="opt">Home Buyer</div>
        <div class="opt">Mortgage Lender</div>
      </div>
      <span class="btn apply">Apply Now</span>
    </div>
  </form>
  <div class="trust"><span class="ico"></span>Trusted as the largest group of experienced mortgage brokers serving home buyers across Canada.<span class="cta">APPLY NOW</span></div>
</header>

<h2 class="sec-title" style="top:590px">WHY USE A MORTGAGE BROKER?</h2>

<article class="why-card" style="left:60px">
  <div class="photo" role="img" aria-label="Photo of construction workers in hard hats" style="background:linear-gradient(135deg,#7fa6c8,#e0b067)"></div>
  <span class="tag">Experienced Lenders</span>
  <p>A broker compares many lenders for you, finds better rates and handles the paperwork so you can focus on finding the right home for your family.</p>
  <span class="btn">Know More</span>
</article>
<article class="why-card" style="left:430px">
  <div class="photo" role="img" aria-label="Photo of a house with a backyard swimming pool" style="background:linear-gradient(135deg,#4f9fd6,#d8c6a3)"></div>
  <span class="tag">Lower Rates</span>
  <p>Brokers work with banks and private lenders nationwide, giving you access to rates and terms that are not offered directly to the public.</p>
  <span class="btn">Know More</span>
</article>
<article class="why-card" style="left:800px">
  <div class="photo" role="img" aria-label="Photo of a couple meeting with an advisor" style="background:linear-gradient(135deg,#c99a72,#e9dcc8)"></div>
  <span class="tag">Personal Advice</span>
  <p>Get honest guidance from one advisor from application to closing, with clear answers about payments, terms and options at every step.</p>
  <span class="btn">Know More</span>
</article>

<section class="areyou" role="img" aria-label="Photo of a large white house with garden and blue sky">
  <h2>ARE YOU A</h2>
  <div class="role" style="left:90px">
    <div class="badge"><svg width="30" height="30" viewBox="0 0 30 30"><circle cx="15" cy="10" r="6" fill="#fff"/><path d="M4 27c1-7 6-10 11-10s10 3 11 10z" fill="#fff"/></svg></div>
    <h3>HOME BUYERS</h3>
    <p>Buying your first home? Learn about down payments, pre-approval and programs made for first time buyers.</p>
  </div>
  <div class="role" style="left:450px">
    <div class="badge"><svg width="30" height="30" viewBox="0 0 30 30"><path d="M4 14 15 5l11 9v12H4z" fill="none" stroke="#fff" stroke-width="2.5"/><rect x="12" y="17" width="6" height="9" fill="#fff"/></svg></div>
    <h3>REFINANCE OPTIONS</h3>
    <p>Lower your payments, consolidate debt or access equity with a refinance that fits your goals.</p>
  </div>
  <div class="role" style="left:810px">
    <div class="badge"><svg width="30" height="30" viewBox="0 0 30 30"><rect x="6" y="4" width="18" height="22" rx="2" fill="none" stroke="#fff" stroke-width="2.5"/><path d="M10 15l4 4 7-8" fill="none" stroke="#fff" stroke-width="2.5"/></svg></div>
    <h3>PURCHASE OPTIONS</h3>
    <p>Second home or new purchase, explore flexible terms and find the mortgage that suits your plans.</p>
  </div>
  <span class="btn role-btn" style="left:185px;background:var(--blue)">CLICK HERE</span>
  <span class="btn role-btn" style="left:545px;background:var(--orange)">CLICK HERE</span>
  <span class="btn role-btn" style="left:905px;background:var(--green)">CLICK HERE</span>
</section>

<h2 class="sec-title" style="top:1560px">REAL ESTATE PROPERTY</h2>

<div class="prop" style="left:60px;top:1620px"><div class="photo" role="img" aria-label="Photo of a villa with a pool" style="background:linear-gradient(135deg,#c98a4b,#e8c98f)"><span class="corner"></span></div><div class="meta"><span class="name">Maple Ridge Homes</span><span class="btn view">View Property</span></div></div>
<div class="prop" style="left:342px;top:1620px"><div class="photo" role="img" aria-label="Photo of a stucco house exterior" style="background:linear-gradient(135deg,#e6d2a8,#b98b5c)"><span class="corner"></span></div><div class="meta"><span class="name">Maple Ridge Homes</span><span class="btn view">View Property</span></div></div>
<div class="prop" style="left:624px;top:1620px"><div class="photo" role="img" aria-label="Photo of a modern home at twilight" style="background:linear-gradient(135deg,#5a6f8e,#d59b62)"><span class="corner"></span></div><div class="meta"><span class="name">Maple Ridge Homes</span><span class="btn view">View Property</span></div></div>
<div class="prop" style="left:906px;top:1620px"><div class="photo" role="img" aria-label="Photo of a seaside house with palm trees" style="background:linear-gradient(135deg,#6fb0de,#d7e3ea)"><span class="corner"></span></div><div class="meta"><span class="name">Maple Ridge Homes</span><span class="btn view">View Property</span></div></div>

<div class="prop" style="left:60px;top:1860px"><div class="photo" role="img" aria-label="Photo of a house with lawn" style="background:linear-gradient(135deg,#8fae6a,#d8c3a0)"><span class="corner"></span></div><div class="meta"><span class="name">Maple Ridge Homes</span><span class="btn view">View Property</span></div></div>
<div class="prop" style="left:342px;top:1860px"><div class="photo" role="img" aria-label="Photo of a brick family home" style="background:linear-gradient(135deg,#b66f4c,#e4c6a4)"><span class="corner"></span></div><div class="meta"><span class="name">Maple Ridge Homes</span><span class="btn view">View Property</span></div></div>
<div class="prop" style="left:624px;top:1860px"><div class="photo" role="img" aria-label="Photo of a white villa against blue sky" style="background:linear-gradient(135deg,#78a8d4,#efe6d6)"><span class="corner"></span></div><div class="meta"><span class="name">Maple Ridge Homes</span><span class="btn view">View Property</span></div></div>
<div class="prop" style="left:906px;top:1860px"><div class="photo" role="img" aria-label="Photo of a townhouse row" style="background:linear-gradient(135deg,#d6a173,#9fb9d2)"><span class="corner"></span></div><div class="meta"><span class="name">Maple Ridge Homes</span><span class="btn view">View Property</span></div></div>

<footer class="footer">
  <div class="brand"><span class="brand-dot"></span>Quellbrin</div>
  <div class="fcol" style="left:260px"><h4>About Quellbrin</h4>Our Story<br>Terms Of Use<br>Privacy Policy</div>
  <div class="fcol" style="left:440px"><h4>For Home Buyers</h4>Home<br>Services<br>MLS Search</div>
  <div class="fcol" style="left:620px"><h4>For Developers</h4>Mortgage Rates<br>Contact<br>Featured Listings</div>
  <div class="fcol" style="left:800px"><h4>For Lenders</h4>Financial Listings<br>Mortgage Calculator<br>Resources</div>
  <div class="fcol" style="left:980px"><h4>Insurance</h4>Home<br>Auto<br>Life<br>Business</div>
  <div class="join">Join us <span class="c"></span><span class="c"></span><span class="c"></span><span class="c"></span></div>
  <div class="subscribe">Subscribe to our Newsletter <span class="in">Enter Your Email</span><span class="btn go">Go</span></div>
  <div class="copy">Copyright Quellbrin.ca Mortgage © 2024. All Rights Reserved. www.quellbrin.ca</div>
</footer>

</body>
</html>
```